Quendaro Pet Store Web Template

We need a new web design for an online Pet Store based in Australia but looking to expand internationally in the future.

The template HTML & CSS should be easily integrated into a quendaro web-store.

We sell a wide range of high quality pet products to our customers at competitive prices.This is our unique selling point.

We intend to become a market leader hence our brand has to look the part with simple yet outstanding icons.

The overall design has to be more visually appealing and simpler than our competitors and lead to a higher conversion rate.

The following are our biggest competitors:
www.tailnook.example
www.pawmeadow.example
www.critterloft.example

Of our competitors www.critterloft.example has the feel that we intend to have but obviously it has to be unique & iconic.

In short our web design has to be associated with Leading,Trust & Quality.

Please find attached Logo so that the site color theme can blend with the logo.

Target Market(s)

Online Pet Products shoppers worldwide

Industry/Entity Type

Pet

Coding

Coded - Design and coding required

Number of Pages Required

3 page

Font styles to use
Sans Serif

Requirements
Must have
• Check out page design.
• Product description menus(when you click on the product)
• Categories should be the same and should be hid or un-hidden by admin.
• Color theme will depend on the final logo to be completed soon.
Nice to have
• Please find attached logo.The site should blend well with logo.

```html
<!DOCTYPE html>
<html lang="en">
<head>
<meta charset="utf-8">
<title>Pawvista – Pet Store</title>
<link rel="stylesheet" href="https://fonts.googleapis.com/css2?family=Open+Sans:ital,wght@0,400;0,600;0,700;1,600&family=Dancing+Script:wght@700&display=swap">
<style>
:root{
  --page:#fdf6ee;
  --frame:#fbe3c9;
  --teal:#5bbccc;
  --red:#f0474f;
  --dog:#4f9a34;
  --cat:#8db516;
  --bird:#1aa3d9;
  --reptile:#1766b1;
  --fish:#e2391b;
  --small:#f5861f;
  --gifts:#f7a11a;
  --green:#6aab2e;
  --text:#555;
  --muted:#888;
  --orange:#f57f20;
  --white:#fff;
}
*{box-sizing:border-box;margin:0;padding:0}
html,body{width:1200px;height:2232px;overflow:hidden}
body{background:var(--frame);font-family:"Open Sans",Arial,sans-serif;color:var(--text);position:relative}
.page{position:absolute;left:29px;top:0;width:1142px;height:2232px;background:var(--page)}
.abs{position:absolute}

/* top bar */
.topbar{left:0;top:0;width:1142px;height:42px;background:var(--teal);color:var(--white);font-size:13px}
.topbar .locale{left:0;top:0;width:153px;height:42px;background:var(--red);display:flex;align-items:center;gap:44px;padding-left:22px}
.topbar .links{left:152px;top:0;height:42px;display:flex;align-items:center;gap:22px}
.topbar .welcome{right:22px;top:0;height:42px;line-height:42px}

/* categories */
.catnav{left:0;top:44px;width:1142px;height:44px;display:flex}
.catnav a{flex:1;color:var(--white);text-decoration:none;font-size:12px;font-weight:600;display:flex;align-items:center;justify-content:center;text-transform:uppercase}

/* header */
.logo{left:20px;top:108px;display:flex;align-items:center;gap:10px}
.logo .mark{width:30px;height:30px;border-radius:50%;background:var(--red)}
.logo .name{font-size:26px;font-weight:700;color:#444}
.cart{left:784px;top:126px;height:28px;display:flex;align-items:center;gap:10px;font-size:12px;color:#444}
.search{left:918px;top:126px;width:202px;height:28px;border:1px solid #ddd;background:var(--white);font-size:11px;color:#777;padding:0 10px;display:flex;align-items:center;justify-content:space-between}

/* banners */
.banner{overflow:hidden}
.hero{left:19px;top:193px;width:551px;height:423px;background:radial-gradient(ellipse at 45% 55%,#c08a4e 0,#8a5a2e 28%,#4c7a2a 60%,#2f5a1a 100%)}
.slider-arrows{right:18px;bottom:14px;display:flex;gap:4px}
.slider-arrows span{width:26px;height:26px;background:rgba(255,255,255,.6);display:flex;align-items:center;justify-content:center}
.dogfood{left:576px;top:193px;width:283px;height:423px;background:var(--white)}
.dogfood h2{position:absolute;top:40px;width:100%;text-align:center;color:var(--bird);font-size:34px;font-weight:600}
.dogfood .save{position:absolute;top:84px;width:100%;text-align:center;color:var(--bird);font:700 32px "Dancing Script",cursive}
.dogfood .photo{position:absolute;left:40px;top:140px;width:190px;height:270px;background:radial-gradient(ellipse at 50% 50%,#f3e7d6 0,#e9d7bd 55%,#fff 75%)}
.dogfood .shop{position:absolute;left:176px;top:168px;width:84px;height:84px;border-radius:50%;background:var(--small);color:var(--white);font-size:15px;font-weight:600;display:flex;align-items:center;justify-content:center}
.reptile{left:867px;top:193px;width:256px;height:423px;background:#050505}
.reptile h2{position:absolute;left:28px;top:36px;color:var(--white);font-size:42px;font-weight:600;line-height:1.22}
.reptile .save{position:absolute;left:30px;top:150px;color:var(--small);font:700 30px "Dancing Script",cursive}
.reptile .photo{position:absolute;left:20px;top:260px;width:236px;height:150px;background:radial-gradient(ellipse at 55% 50%,#f28a1e 0,#c8561a 40%,#050505 72%)}
.aquarium{left:19px;top:624px;width:551px;height:239px;background:#1383c4}
.aquarium .photo{position:absolute;left:0;top:0;width:290px;height:239px;background:radial-gradient(ellipse at 40% 45%,#f2c22a 0,#e58b1e 22%,#1383c4 52%)}
.aquarium .copy{position:absolute;left:298px;top:38px;color:var(--white);font-weight:700;line-height:1.18}
.aquarium .copy .new{color:#9ee0f5;font-size:40px;display:block;margin-bottom:4px}
.aquarium .copy span{font-size:31px}
.clothing{left:576px;top:624px;width:547px;height:239px;background:#f6b6cd}
.clothing .photo{position:absolute;left:0;top:0;width:280px;height:239px;background:radial-gradient(ellipse at 45% 45%,#c08a6a 0,#e9a8c0 40%,#f6b6cd 70%)}
.clothing .badge{position:absolute;left:333px;top:24px;width:116px;height:116px;border-radius:50%;background:var(--white);padding:6px}
.clothing .badge div{width:100%;height:100%;border-radius:50%;background:#ef5d8c;color:var(--white);display:flex;flex-direction:column;align-items:center;justify-content:center;line-height:1}
.clothing .badge .f{font:700 24px "Dancing Script",cursive}
.clothing .badge .s{font-size:30px;font-weight:700}
.clothing .copy{position:absolute;left:270px;top:146px;width:277px;text-align:center;color:var(--white);font-size:29px;font-weight:700;line-height:1.2}

/* products */
.section-title{left:25px;width:1083px;height:33px;color:var(--white);font-size:15px;padding-left:14px;line-height:33px;text-transform:uppercase}
.section-title.special{top:909px;background:var(--red)}
.section-title.new{top:1372px;background:var(--teal)}
.grid{left:67px;width:1000px;display:flex;gap:52px}
.grid.special{top:970px}
.grid.new{top:1445px}
.card{width:211px;height:372px;background:var(--white);padding:0 18px}
.card .img{height:230px;margin:0 -18px;display:flex;align-items:center;justify-content:center}
.card .img div{width:160px;height:180px;border-radius:6px}
.card h3{color:var(--green);font-size:14px;font-weight:600;margin-top:4px}
.card p{font-size:11px;line-height:1.65;margin-top:6px;color:var(--text)}
.card .row{display:flex;justify-content:space-between;align-items:flex-end;margin-top:6px}
.card .old{font-size:12px;color:var(--muted);text-decoration:line-through;display:block}
.card .price{font-size:16px;color:var(--red);display:block}
.card .btn{display:flex;height:22px;margin-bottom:1px}
.card .btn i{width:22px;background:var(--red);display:flex;align-items:center;justify-content:center}
.card .btn b{background:var(--teal);color:var(--white);font-size:10px;font-weight:600;padding:0 12px;line-height:22px}

/* footer */
.footer{left:0;top:1885px;width:1142px;height:298px;background:#fef5ea}
.fcol{top:30px;width:270px;height:240px;padding-left:0}
.fcol.sep{border-right:1px solid #ccc}
.fcol h4{color:var(--small);font-size:11px;font-weight:400;text-transform:uppercase;margin-bottom:20px}
.fcol li{list-style:none;font-size:11px;color:#555;line-height:24.5px}
.newsletter{width:252px;height:32px;border:1px solid #ddd;background:var(--white);font-size:11px;color:#888;padding:0 10px;display:flex;align-items:center;justify-content:space-between}
.social{display:flex;gap:12px;margin-top:14px}
.social span{width:36px;height:36px;border-radius:50%;background:var(--cat)}
.bottombar{left:0;top:2193px;width:1142px;height:39px;background:var(--orange);color:var(--white);font-size:11px;line-height:39px;padding-left:26px}
</style>
</head>
<body>
<div class="page">

  <div class="abs topbar">
    <div class="abs locale"><span>En ▾</span><span>$ ▾</span></div>
    <nav class="abs links"><span>My Account</span><span>My Wishlist</span><span>Checkout</span><span>Log in</span></nav>
    <div class="abs welcome">Welcome to our online store</div>
  </div>

  <nav class="abs catnav">
    <a style="background:var(--dog)">Dog</a>
    <a style="background:var(--cat)">Cat</a>
    <a style="background:var(--bird)">Bird</a>
    <a style="background:var(--reptile)">Reptile</a>
    <a style="background:var(--fish)">Fish</a>
    <a style="background:var(--small)">Small Animal</a>
    <a style="background:var(--gifts)">Gifts</a>
  </nav>

  <div class="abs logo"><span class="mark"></span><span class="name">Pawvista</span></div>
  <div class="abs cart">
    <svg width="20" height="16" viewBox="0 0 20 16"><path d="M1 2h3l2 9h10l2-7H5" fill="none" stroke="#e2391b" stroke-width="2"/><circle cx="8" cy="14" r="1.6" fill="#e2391b"/><circle cx="15" cy="14" r="1.6" fill="#e2391b"/></svg>
    <span>0 item(s) - $0.00</span>
  </div>
  <div class="abs search"><span>Search entire store here...</span>
    <svg width="12" height="12" viewBox="0 0 12 12"><circle cx="5" cy="5" r="3.6" fill="none" stroke="#888" stroke-width="1.4"/><path d="M8 8l3 3" stroke="#888" stroke-width="1.4"/></svg>
  </div>

  <div class="abs banner hero" role="img" aria-label="Photo of two puppies resting on a log">
    <div class="abs slider-arrows"><span>‹</span><span>›</span></div>
  </div>
  <div class="abs banner dogfood">
    <h2>DOG FOOD</h2>
    <div class="save">Save 15%</div>
    <div class="photo" role="img" aria-label="Photo of a sitting puppy"></div>
    <div class="shop">Shop</div>
  </div>
  <div class="abs banner reptile">
    <h2>Reptile<br>Products</h2>
    <div class="save">Save 20%</div>
    <div class="photo" role="img" aria-label="Photo of an orange and black frog"></div>
  </div>
  <div class="abs banner aquarium">
    <div class="photo" role="img" aria-label="Photo of a tropical fish over coral"></div>
    <div class="copy"><span class="new">New!</span><span>Natural<br>LED Aquarium<br>Lighting</span></div>
  </div>
  <div class="abs banner clothing">
    <div class="photo" role="img" aria-label="Photo of a small dog in a pink outfit with flowers"></div>
    <div class="badge"><div><span class="f">Final</span><span class="s">SALE</span></div></div>
    <div class="copy">Dog Clothing &amp;<br>Accessories</div>
  </div>

  <h2 class="abs section-title special">Special Products</h2>
  <div class="abs grid special">
    <div class="card"><div class="img"><div role="img" aria-label="Grooming tote bag" style="background:linear-gradient(#7a5a48,#4e3a30)"></div></div>
      <h3>Grooming Tode</h3><p>Lorem ipsum dolor sit amet conse ctetur adipisicing elit, sed do eiusmod</p>
      <div class="row"><div><span class="old">$ 120.00</span><span class="price">$ 102.00</span></div><span class="btn"><i>🛒</i><b>DETAILS</b></span></div></div>
    <div class="card"><div class="img"><div role="img" aria-label="Yellow litter bucket" style="background:linear-gradient(#2eb6d8 0,#2eb6d8 15%,#f2e22a 15%,#e9d21e)"></div></div>
      <h3>Neat Litter</h3><p>Lorem ipsum dolor sit amet conse ctetur adipisicing elit, sed do eiusmod</p>
      <div class="row"><div><span class="old">$ 110.00</span><span class="price">$ 92.00</span></div><span class="btn"><i>🛒</i><b>DETAILS</b></span></div></div>
    <div class="card"><div class="img"><div role="img" aria-label="Green bathing brushes" style="background:linear-gradient(135deg,#f5c21a,#8ed12a 50%,#2b2b2b)"></div></div>
      <h3>Suds Tub Bathing Brush</h3><p>Lorem ipsum dolor sit amet conse ctetur adipisicing elit, sed do eiusmod</p>
      <div class="row"><div><span class="old">$ 130.00</span><span class="price">$ 112.00</span></div><span class="btn"><i>🛒</i><b>DETAILS</b></span></div></div>
    <div class="card"><div class="img"><div role="img" aria-label="Blue bath gloves" style="background:linear-gradient(#4fc3d8,#2aa9c4)"></div></div>
      <h3>Bath Gloves</h3><p>Lorem ipsum dolor sit amet conse ctetur adipisicing elit, sed do eiusmod</p>
      <div class="row"><div><span class="old">$ 120.00</span><span class="price">$ 105.00</span></div><span class="btn"><i>🛒</i><b>DETAILS</b></span></div></div>
  </div>

  <h2 class="abs section-title new">New Products</h2>
  <div class="abs grid new">
    <div class="card"><div class="img"><div role="img" aria-label="Four coat spray bottles" style="background:linear-gradient(90deg,#f2a21e,#5cb8d8,#f27e2a,#8cc43a)"></div></div>
      <h3>Baby powder scent spray</h3><p>Lorem ipsum dolor sit amet conse ctetur adipisicing elit, sed do eiusmod</p>
      <div class="row"><div><span class="old">$ 220.00</span><span class="price">$ 200.00</span></div><span class="btn"><i>🛒</i><b>DETAILS</b></span></div></div>
    <div class="card"><div class="img"><div role="img" aria-label="Small dog in a blue bathrobe" style="background:linear-gradient(#e6d2b8,#5ab9d6 45%,#4aa8c6)"></div></div>
      <h3>Neat Litter</h3><p>Lorem ipsum dolor sit amet conse ctetur adipisicing elit, sed do eiusmod</p>
      <div class="row"><div><span class="old">$ 120.00</span><span class="price">$ 102.00</span></div><span class="btn"><i>🛒</i><b>DETAILS</b></span></div></div>
    <div class="card"><div class="img"><div role="img" aria-label="Dog wearing a shark hoodie" style="background:linear-gradient(#8fd2e4,#6cc0d8 60%,#3a3a3a)"></div></div>
      <h3>Dog Shark Hoodie</h3><p>Lorem ipsum dolor sit amet conse ctetur adipisicing elit, sed do eiusmod</p>
      <div class="row"><div><span class="old">$ 122.00</span><span class="price">$ 106.00</span></div><span class="btn"><i>🛒</i><b>DETAILS</b></span></div></div>
    <div class="card"><div class="img"><div role="img" aria-label="Blue and black pet carrier" style="background:linear-gradient(#3aa8d8,#2a2a2a)"></div></div>
      <h3>Pet Carrier</h3><p>Lorem ipsum dolor sit amet conse ctetur adipisicing elit, sed do eiusmod</p>
      <div class="row"><div><span class="old">$ 130.00</span><span class="price">$ 112.00</span></div><span class="btn"><i>🛒</i><b>DETAILS</b></span></div></div>
  </div>

  <footer class="abs footer">
    <div class="abs fcol sep" style="left:26px"><h4>Information</h4><ul>
      <li>About US</li><li>Customer Service</li><li>Template Settings</li><li>Privacy Policy</li><li>Site Map</li><li>Search Terms</li><li>Advanced Search</li><li>Orders And Returns</li><li>Contact Us</li></ul></div>
    <div class="abs fcol sep" style="left:306px"><h4>Why buy from us</h4><ul>
      <li>Shipping &amp; Returns</li><li>Secure Shopping</li><li>International Shipping</li><li>Affiliates</li><li>Group Sales</li></ul></div>
    <div class="abs fcol sep" style="left:585px"><h4>My Account</h4><ul>
      <li>Sign In</li><li>View Cart</li><li>My Wishlist</li><li>Track My Order</li><li>Help</li></ul></div>
    <div class="abs fcol" style="left:863px"><h4>News Letter</h4>
      <div class="newsletter"><span>Enter your E-mail Address</span><span>›</span></div>
      <h4 style="margin-top:30px;margin-bottom:0">Follow Us</h4>
      <div class="social"><span></span><span></span><span></span></div>
    </div>
  </footer>
  <div class="abs bottombar">© 2014 - Privacy Policy</div>
</div>
</body>
</html>
```